Business card for wedding & event planning company

I'm looking for a well designed double sided business card to represent my wedding and event planning company.

It should include the fact we manage the following events:
Weddings, birthdays, conferences, product launches, fashion shows & conventions
in the following areas:
Wiltshire, Oxfordshire, Berkshire & London

My contact details to be included are:

Moira Pennock
07715 482036
moira@amberlarkcelebrations.co.uk
www.amberlarkcelebrations.co.uk

My logo can be found at the following Filevaultex location:
AI file: https://www.filevaultex.com/s/k4mprt8wn31b7hz/brandlogo_sourcefile.ai?dl=0
PNG file:
https://www.filevaultex.com/s/h9qsle2vbx07mnd/brandlogo_image.png?dl=0

Target Market(s)

women aged 30-55

Industry/Entity Type

Wedding

Contact Information for Business Card

in the following areas:

Moira Pennock
Event Planner
07715 482036

Font styles to use
Serif
Sans Serif
Script

Requirements
Must have
• Purple and white colour scheme
Should not have
• Black background
• Please don't submit any of the see-through business card designs.

```html
<!DOCTYPE html>
<html lang="en">
<head>
<meta charset="utf-8">
<title>Amber Lark Celebrations – Business Card</title>
<link rel="stylesheet" href="https://fonts.googleapis.com/css2?family=Gentium+Book+Plus:wght@400;700&display=swap">
<style>
  :root {
    --purple: #8b3196;
    --purple-soft: #e7d3eb;
    --white: #ffffff;
    --ink: #1c1c1c;
    --backdrop: #d9d9db;
    --serif: "Gentium Book Plus", Georgia, serif;
  }
  * { box-sizing: border-box; margin: 0; padding: 0; }
  html, body {
    width: 1200px; height: 926px; overflow: hidden;
    background: var(--backdrop);
    font-family: var(--serif);
  }
  .sheet {
    width: 1200px; height: 926px;
    display: flex; flex-direction: column;
    align-items: center; justify-content: center; gap: 34px;
  }
  .card {
    position: relative;
    width: 720px; height: 412px;
    background: var(--white);
    box-shadow: 0 6px 18px rgba(0,0,0,.18);
    overflow: hidden;
  }

  /* Brand lockup */
  .brand { display: flex; align-items: center; gap: 10px; color: var(--purple); }
  .brand-dot {
    width: 14px; height: 14px; border-radius: 50%;
    background: var(--purple);
  }
  .brand-name { font-weight: 400; font-size: 30px; letter-spacing: .5px; }

  /* Back side */
  .card-back .brand-area {
    height: 138px; display: flex; align-items: center; justify-content: center;
  }
  .card-back .info-band {
    position: absolute; left: 0; right: 0; top: 138px; bottom: 26px;
    background: var(--purple); color: var(--white);
    display: flex; flex-direction: column; align-items: center; justify-content: center;
    text-align: center; gap: 10px;
  }
  .info-heading { font-size: 28px; letter-spacing: 2px; line-height: 1; }
  .info-text { font-size: 21px; line-height: 1.25; }
  .info-block + .info-block { margin-top: 12px; }

  /* Front side */
  .card-front .brand { position: absolute; left: 40px; top: 34px; }
  .card-front .brand-name { font-size: 26px; }
  .brand-rule {
    position: absolute; left: 40px; top: 80px; width: 300px; height: 1px;
    background: var(--purple-soft);
  }
  .holder-name {
    position: absolute; left: 52px; top: 120px;
    font-size: 40px; font-weight: 700; color: var(--purple);
  }
  .contact-list {
    position: absolute; left: 62px; top: 222px;
    list-style: none; color: var(--ink); font-size: 21px; line-height: 1.42;
  }
  .emblem-area {
    position: absolute; right: 36px; top: 70px;
    width: 290px; height: 290px; border-radius: 50%;
    background: radial-gradient(circle at 50% 45%, var(--white) 0%, var(--purple-soft) 100%);
    border: 4px solid var(--purple);
  }
</style>
</head>
<body>
  <main class="sheet">
    <section class="card card-back" aria-label="Card back">
      <div class="brand-area">
        <div class="brand">
          <span class="brand-dot"></span>
          <span class="brand-name">Amber Lark Celebrations</span>
        </div>
      </div>
      <div class="info-band">
        <div class="info-block">
          <h2 class="info-heading">EVENTS</h2>
          <p class="info-text">Weddings, birthdays, conferences,<br>product launches, fashion shows &amp; conventions</p>
        </div>
        <div class="info-block">
          <h2 class="info-heading">AREAS</h2>
          <p class="info-text">Wiltshire, Oxfordshire, Berkshire &amp; London</p>
        </div>
      </div>
    </section>

    <section class="card card-front" aria-label="Card front">
      <div class="brand">
        <span class="brand-name">Amber Lark Celebrations</span>
      </div>
      <div class="brand-rule"></div>
      <h1 class="holder-name">Moira Pennock</h1>
      <ul class="contact-list">
        <li>07715 482036</li>
        <li>moira@amberlarkcelebrations.co.uk</li>
        <li>www.amberlarkcelebrations.co.uk</li>
      </ul>
      <div class="emblem-area" role="img" aria-label="Large brand emblem in purple outline within a circle"></div>
    </section>
  </main>
</body>
</html>
```